Very High End Grooming Salon needs new business card design

I need a very nice card design I am a certified Master groomer we have a very high end clients. Our color is pink but does not have to be pink. I have a logo also a mission statement .
Fluff N Fern Pet Boutique and Spa
48810 Marlow Rd
North Palm Beach fl 33471
561 904 3782
www.fluffernboutique.example
online booking available
this is our mission statement not sure it need to go on card but here it is.
Our Mission is to show respect to all animals pampering them with the same high end tailored service one would expect to receive at a day spa
as the only certified master groomer in the area we strive to put your pets best paw forward.

Industry/Entity Type

Business

```html
<!DOCTYPE html>
<html lang="en">
<head>
<meta charset="utf-8">
<title>Fluff 'N Fern Pet Boutique and Spa – Business Card</title>
<link rel="stylesheet" href="https://fonts.googleapis.com/css2?family=Lato:ital,wght@0,400;0,700;1,400&family=Dancing+Script:wght@500&display=swap">
<style>
  :root {
    --stage: #2a2a2a;
    --card: #ffffff;
    --card-edge: #e9e9ec;
    --pink: #d6217a;
    --pink-soft: #f2b6d3;
    --ink: #4a4a4a;
    --muted: #8a8a8a;
  }
  * { margin: 0; padding: 0; box-sizing: border-box; }
  html, body { width: 1200px; height: 900px; overflow: hidden; }
  body {
    background: var(--stage);
    font-family: "Lato", sans-serif;
    position: relative;
  }
  .card {
    position: absolute;
    left: 250px;
    width: 700px;
    height: 400px;
    border-radius: 28px;
    background: linear-gradient(160deg, var(--card) 55%, var(--card-edge));
    box-shadow: 0 10px 30px rgba(0,0,0,.45);
    overflow: hidden;
  }
  .card--back { top: 35px; }
  .card--front { top: 465px; }

  /* brand name lockup */
  .brand {
    position: absolute;
    display: flex;
    align-items: center;
    gap: 14px;
    color: var(--pink);
    font-weight: 700;
    letter-spacing: .5px;
  }
  .brand__dot {
    width: 22px; height: 22px;
    border-radius: 50%;
    background: var(--pink);
    flex: none;
  }
  .brand__name { line-height: 1.15; }

  .card--back .brand { left: 48px; top: 150px; font-size: 30px; }
  .card--front .brand { left: 48px; top: 60px; font-size: 34px; }

  .illustration {
    position: absolute;
    border-radius: 20px;
    background: radial-gradient(circle at 40% 45%, var(--pink-soft), #f8dbe9 70%);
  }
  .card--back .illustration { left: 60px; top: 230px; width: 200px; height: 120px; }
  .card--front .illustration { left: 470px; top: 40px; width: 190px; height: 115px; }

  /* back info */
  .about {
    position: absolute;
    right: 48px;
    top: 48px;
    width: 300px;
    text-align: right;
    color: var(--muted);
    font-size: 15px;
    line-height: 1.35;
  }
  .about p { margin-bottom: 16px; }
  .hours { color: var(--ink); font-size: 15px; line-height: 1.35; }
  .hours__title { color: var(--pink); font-weight: 700; }

  /* front */
  .owner { position: absolute; left: 60px; top: 250px; }
  .owner__name {
    font-family: "Dancing Script", cursive;
    color: var(--pink);
    font-size: 48px;
    line-height: 1;
  }
  .owner__role { color: var(--muted); font-size: 18px; margin-top: 10px; }

  .contact {
    position: absolute;
    left: 400px;
    top: 200px;
    list-style: none;
    color: var(--ink);
    font-size: 17px;
  }
  .contact li { display: flex; align-items: flex-start; gap: 12px; line-height: 1.25; }
  .contact li.gap { margin-bottom: 22px; }
  .contact svg { width: 16px; height: 16px; flex: none; margin-top: 3px; fill: var(--pink); }
</style>
</head>
<body>

<section class="card card--back" aria-label="Card back">
  <div class="brand">
    <span class="brand__dot"></span>
    <span class="brand__name">Fluff 'N Fern</span>
  </div>
  <div class="illustration" role="img" aria-label="Pink ornamental poodle illustration"></div>

  <div class="about">
    <p>All Breeds of dogs and cats are welcome.</p>
    <p>The Fluff 'N Fern groomers take special care of your pets.</p>
    <p>Groomers are attentive to the elderly and disabled pets and pets not used to being in crates.</p>
    <div class="hours">
      <div class="hours__title">Opening Hours</div>
      <div>tue.-fri. 7:30AM – 5PM</div>
      <div>sat. 9:00AM – 5PM</div>
    </div>
  </div>
</section>

<section class="card card--front" aria-label="Card front">
  <div class="brand">
    <span class="brand__dot"></span>
    <span class="brand__name">Fluff 'N Fern<br>Pet Boutique and Spa</span>
  </div>
  <div class="illustration" role="img" aria-label="Pink ornamental poodle illustration"></div>

  <div class="owner">
    <div class="owner__name">Dana Whitlow</div>
    <div class="owner__role">founder and owner</div>
  </div>

  <ul class="contact">
    <li class="gap">
      <svg viewBox="0 0 16 16" aria-hidden="true"><path d="M8 0a5.5 5.5 0 0 0-5.5 5.5C2.5 10 8 16 8 16s5.5-6 5.5-10.5A5.5 5.5 0 0 0 8 0zm0 8a2.5 2.5 0 1 1 0-5 2.5 2.5 0 0 1 0 5z"/></svg>
      <span>48810 Marlow Rd<br>North Palm Beach, FL 33471</span>
    </li>
    <li>
      <svg viewBox="0 0 16 16" aria-hidden="true"><path d="M3.6 1l2.6 3-1.5 1.8a9 9 0 0 0 5.5 5.5L12 9.8l3 2.6-1.6 2.6C7.500 14.8 1.200 8.500 1 2.600z"/></svg>
      <span>(561) 904-3782</span>
    </li>
    <li>
      <svg viewBox="0 0 16 16" aria-hidden="true"><path d="M1 3h14v10H1zM1.8 3.8L8 8.600l6.2-4.8v1.4L8 10 1.8 5.200z" fill-rule="evenodd"/></svg>
      <span>dana@fluffernboutique.example</span>
    </li>
    <li>
      <svg viewBox="0 0 16 16" aria-hidden="true"><path d="M8 1a7 7 0 1 0 0 14A7 7 0 0 0 8 1zm0 1.3c.9 0 1.800 1.700 2 4.200H6C6.200 4 7.100 2.300 8 2.300zM2.400 7.500h2.600c0 .4 0 .8.1 1H2.400a5.700 5.700 0 0 1 0-1zm8.600 0h2.600a5.700 5.700 0 0 1 0 1H11c.1-.2.1-.6 0-1zM6 9.500h4c-.2 2.500-1.100 4.200-2 4.200s-1.800-1.700-2-4.200z"/></svg>
      <span>www.fluffernboutique.example</span>
    </li>
  </ul>
</section>

</body>
</html>
```